Criação de Kit com 6 Layouts de Post para Redes Sociais (Facebook, Instagram e etc) + Capa de Facebook para Outros
" Atualmente, on-line. Estamos abertos há poucos meses, fazendo atendimento para outras agencias e agora vamos abrir para atendimento do público utilizando instagram, whatsapp e face como formas de captação. "

```html
<!DOCTYPE html>
<html lang="pt-BR">
<head>
<meta charset="UTF-8">
<title>Bora viajar? – Post</title>
<link href="https://fonts.googleapis.com/css2?family=Poppins:wght@400;500;600;700;800&display=swap" rel="stylesheet">
<style>
  :root {
    --sky-top: #e9eef3;
    --sky-mid: #f4f6f8;
    --sky-low: #dfe6ee;
    --brand-blue: #2a9df4;
    --brand-blue-light: #3fb0f7;
    --navy: #0f2a5c;
    --white: #ffffff;
    --photo-a: #8fc6ec;
    --photo-b: #3a9fe0;
    --photo-c: #5f6b78;
  }
  * { margin: 0; padding: 0; box-sizing: border-box; }
  html, body { width: 1200px; height: 1200px; overflow: hidden; }
  body { font-family: 'Poppins', sans-serif; }

  .post {
    position: relative;
    width: 1200px;
    height: 1200px;
    overflow: hidden;
    background:
      radial-gradient(ellipse 500px 260px at 850px 180px, rgba(255,255,255,.9), transparent 70%),
      radial-gradient(ellipse 600px 300px at 950px 1050px, rgba(255,255,255,.85), transparent 70%),
      radial-gradient(ellipse 400px 220px at 300px 1100px, rgba(255,255,255,.7), transparent 70%),
      linear-gradient(180deg, var(--sky-top) 0%, var(--sky-mid) 55%, var(--sky-low) 100%);
  }

  .sky-photo { position: absolute; inset: 0; }

  .side-word {
    position: absolute;
    left: 265px;
    top: -70px;
    transform-origin: 0 0;
    transform: rotate(90deg);
    font-weight: 800;
    font-size: 330px;
    line-height: 1;
    letter-spacing: 10px;
    color: var(--brand-blue);
    white-space: nowrap;
  }

  .flight-path { position: absolute; inset: 0; }

  .bus-photo {
    position: absolute;
    left: 0;
    top: 283px;
    width: 630px;
    height: 672px;
    border-radius: 0 44px 44px 0;
    background:
      linear-gradient(180deg, transparent 72%, var(--photo-c) 72%, #7c8693 100%),
      linear-gradient(135deg, var(--photo-a) 0%, var(--photo-b) 60%, #2b86c8 100%);
  }

  .headline__tag {
    position: absolute;
    left: 920px;
    top: 509px;
    transform: translateX(-50%);
    background: var(--navy);
    color: var(--white);
    font-weight: 700;
    font-size: 56px;
    line-height: 1;
    padding: 8px 26px 6px;
    border-radius: 10px;
    letter-spacing: 1px;
  }
  .headline__main {
    position: absolute;
    left: 690px;
    top: 574px;
    width: 460px;
    text-align: center;
    color: var(--brand-blue);
    font-weight: 700;
    font-size: 128px;
    line-height: 1;
    letter-spacing: -2px;
    white-space: nowrap;
  }
  .headline__sub {
    position: absolute;
    left: 690px;
    top: 748px;
    width: 460px;
    text-align: center;
    color: var(--navy);
    font-weight: 400;
    font-size: 40px;
    line-height: 1.28;
    white-space: nowrap;
  }

  .cta {
    position: absolute;
    left: 752px;
    top: 888px;
    display: flex;
    height: 54px;
  }
  .cta__icon {
    width: 54px;
    height: 54px;
    background: var(--navy);
    border-radius: 6px 0 0 6px;
    display: flex;
    align-items: center;
    justify-content: center;
  }
  .cta__label {
    background: var(--brand-blue-light);
    color: var(--white);
    font-weight: 500;
    font-size: 22px;
    padding: 0 22px;
    display: flex;
    align-items: center;
    border-radius: 0 6px 6px 0;
  }

  .brand-name {
    position: absolute;
    left: 492px;
    top: 1084px;
    color: var(--brand-blue);
    font-weight: 700;
    font-size: 36px;
    letter-spacing: 1px;
  }
</style>
</head>
<body>
<main class="post">
  <div class="sky-photo" role="img" aria-label="Céu claro com nuvens suaves ao fundo"></div>

  <div class="side-word" aria-hidden="true">VIAJAR</div>

  <svg class="flight-path" width="1200" height="1200" viewBox="0 0 1200 1200" aria-hidden="true">
    <g fill="none" stroke="var(--brand-blue)" stroke-width="4" stroke-dasharray="14 12" stroke-linecap="round">
      <path d="M330 40 C 480 130, 520 210, 700 170 S 900 110, 1010 135"/>
      <path d="M0 1165 C 160 1100, 260 1060, 420 1120 S 700 1210, 830 1080 S 1070 1040, 1200 1110"/>
    </g>
    <g fill="var(--brand-blue)">
      <g transform="translate(1060 130) rotate(10)">
        <path d="M-50 -6 L30 -6 Q50 0 30 6 L-50 6 Z"/>
        <path d="M-6 -6 L-30 -48 L-14 -48 L18 -6 Z"/>
        <path d="M-6 6 L-30 48 L-14 48 L18 6 Z"/>
        <path d="M-50 -5 L-60 -22 L-50 -22 L-38 -5 Z"/>
        <path d="M-50 5 L-60 22 L-50 22 L-38 5 Z"/>
      </g>
      <g transform="translate(350 1160) rotate(-20)">
        <path d="M-50 -6 L30 -6 Q50 0 30 6 L-50 6 Z"/>
        <path d="M-6 -6 L-30 -48 L-14 -48 L18 -6 Z"/>
        <path d="M-6 6 L-30 48 L-14 48 L18 6 Z"/>
        <path d="M-50 -5 L-60 -22 L-50 -22 L-38 -5 Z"/>
        <path d="M-50 5 L-60 22 L-50 22 L-38 5 Z"/>
      </g>
    </g>
  </svg>

  <div class="bus-photo" role="img" aria-label="Ônibus de turismo azul estacionado em pátio asfaltado"></div>

  <span class="headline__tag">BORA</span>
  <h1 class="headline__main">viajar?</h1>
  <p class="headline__sub">Conheça vários<br>destinos com a gente!</p>

  <div class="cta">
    <span class="cta__icon">
      <svg width="22" height="26" viewBox="0 0 22 26" aria-hidden="true">
        <path d="M5 3 L16 13 L5 23" fill="none" stroke="var(--white)" stroke-width="4" stroke-linecap="round" stroke-linejoin="round"/>
      </svg>
    </span>
    <span class="cta__label">Fale conosco agora!</span>
  </div>

  <div class="brand-name">SEU LOGO</div>
</main>
</body>
</html>
```